Peter Lasko-Wren Finance

Need a personal website advertising Equipment Finance,Business Finance,Commercial Finance, Construction Finance, Bridging Finance. Similar websites are www.varoplend.com.au / www.kitmoxa.com.au / www.rzb4.com.au /wwwbelvaxcredit.com.au

Target Market(s)

Business People

Industry/Entity Type

Business

Number of Pages Required

3 page

Font styles to use
Serif
Sans Serif

Requirements
Must have
• All i want is a simple corporate looking website advertising Equipment Finance, Commercial Finance, Construction Finance, Business Finance, Bridging Finance,

```html
<!DOCTYPE html>
<html lang="en">
<head>
<meta charset="utf-8">
<title>Peter Lasko-Wren Finance – Contact Us</title>
<link href="https://fonts.googleapis.com/css2?family=Montserrat:wght@300;400;600&family=Roboto:wght@400;700&display=swap" rel="stylesheet">
<style>
:root{
  --topbar:#0a7aae;
  --nav:#135c7c;
  --nav-active:#3bb6e6;
  --quote:#29aee3;
  --search:#e4e4e4;
  --ink:#1d5f80;
  --panel-head:#5a8aa0;
  --panel:#165d7e;
  --cta:#f49f16;
  --cta-edge:#f7c04a;
  --dark:#222;
  --muted:#888;
  --line:#e6e6e6;
  --white:#fff;
}
*{box-sizing:border-box;margin:0;padding:0}
html,body{width:1119px;height:1200px;overflow:hidden;background:var(--white)}
body{position:relative;font-family:"Montserrat",Arial,sans-serif;font-weight:300;color:var(--dark)}
.abs{position:absolute}

.topbar{left:0;top:0;width:1119px;height:42px;background:var(--topbar);color:var(--white);font-size:12px;font-weight:400}
.topbar .links{left:40px;top:14px}
.topbar .phone{left:592px;top:14px}
.topbar .social{right:40px;top:10px;display:flex;gap:3px}
.topbar .social span{width:18px;height:18px;border-radius:50%;background:var(--white)}

.brand{left:40px;top:66px;display:flex;align-items:center;gap:14px}
.brand .mark{width:34px;height:34px;border-radius:50%;background:#111}
.brand .name{font-size:31px;font-weight:300;color:#111;letter-spacing:.3px}
.search{left:589px;top:62px;width:322px;height:44px;background:var(--search);border-radius:3px}
.search svg{position:absolute;right:14px;top:11px}
.quote{left:925px;top:62px;width:154px;height:44px;background:var(--quote);color:var(--white);border-radius:3px;font-size:17px;font-weight:400;display:flex;align-items:center;justify-content:center}

.nav{left:0;top:130px;width:1119px;height:53px;background:var(--nav);display:flex}
.nav a{height:53px;display:flex;align-items:center;justify-content:center;color:var(--white);font-size:16px;font-weight:400;text-decoration:none;border-right:1px solid var(--white)}
.nav a:last-child{border-right:0}
.nav a.active{color:var(--nav-active)}

.callout{left:0;top:228px;width:1119px;display:flex;justify-content:center;align-items:center;gap:22px;color:var(--ink);font-size:25px;font-weight:300}

.photo{left:40px;width:356px;height:101px}
.photo.meeting{top:327px;background:linear-gradient(180deg,#c9c6bd 0%,#8f8a80 45%,#d9a66b 70%,#3b3b3b 100%)}
.photo.laptop{top:619px;background:linear-gradient(90deg,#7f5d43 0%,#c9c4bc 30%,#b88e68 60%,#e4e4e2 100%)}
.office{left:40px;color:var(--ink);font-size:13.5px;font-weight:400;line-height:25px}
.office.gold{top:446px}
.office.sydney{top:745px}

.consult{left:538px;top:324px;width:542px;height:545px;background:var(--panel)}
.consult .head{height:76px;background:var(--panel-head);color:var(--white);font-weight:600;font-size:18px;display:flex;align-items:center;justify-content:center;letter-spacing:.3px}
.consult .toolkit{position:absolute;left:150px;top:96px;width:230px;height:248px;background:linear-gradient(180deg,#1e6787 0%,#1e6787 30%,#dce9ef 30%,#cfdfe7 100%);border:3px solid #eef3f5}
.consult input{position:absolute;left:96px;width:343px;height:46px;border:0;padding:0 16px;font-family:"Roboto",Arial,sans-serif;font-size:14px;color:#777;background:var(--white)}
.consult input::placeholder{color:#777}
.consult .f-name{top:355px}
.consult .f-mail{top:412px}
.consult .send{position:absolute;left:96px;top:469px;width:343px;height:52px;background:var(--cta);border:2px solid var(--cta-edge);color:var(--white);font-family:"Roboto",Arial,sans-serif;font-weight:700;font-size:16px;display:flex;align-items:center;justify-content:center}

.rule{left:40px;top:887px;width:1040px;height:4px;background:var(--nav)}

.footer-label{left:38px;top:942px;font-size:12px;font-weight:400}
.pay-badge{left:42px;top:972px;width:158px;height:48px;border:1px solid #ddd;border-radius:3px;display:flex;align-items:center;justify-content:center;gap:6px}
.pay-badge span{width:30px;height:20px;border-radius:3px;background:#d7dde4}
.contact-info{left:268px;top:946px;font-size:12px;font-weight:400;line-height:17px}
.contact-info .row{display:flex;gap:13px;margin-bottom:15px}
.contact-info svg{flex:none}
.foot-nav{right:40px;top:945px;font-size:12px;font-weight:400;text-align:right;line-height:30px}
.foot-nav .primary a{margin-left:15px;color:var(--dark);text-decoration:none}
.foot-nav .primary a.current{color:var(--muted)}

.divider{left:0;top:1088px;width:1119px;height:1px;background:var(--line)}
.legal{left:40px;top:1118px;font-size:12px;font-weight:400;line-height:25px}
.follow{right:40px;top:1121px;display:flex;align-items:center;gap:6px;font-size:12px;font-weight:400}
.follow .label{margin-right:12px}
.follow span.dot{width:24px;height:24px;border-radius:50%;background:#c9c9c9}
</style>
</head>
<body>

<div class="abs topbar">
  <div class="abs links">E-Book - Downloads Sitemap</div>
  <div class="abs phone">T: 1000 000 000</div>
  <div class="abs social"><span></span><span></span><span></span><span></span></div>
</div>

<div class="abs brand">
  <span class="mark"></span>
  <span class="name">Peter Lasko-Wren Finance</span>
</div>
<div class="abs search">
  <svg width="22" height="22" viewBox="0 0 22 22"><rect width="22" height="22" rx="4" fill="#29aee3"/><circle cx="10" cy="10" r="5" fill="none" stroke="#fff" stroke-width="2"/><line x1="13.5" y1="13.5" x2="17" y2="17" stroke="#fff" stroke-width="2.4" stroke-linecap="round"/></svg>
</div>
<div class="abs quote">Quote Now</div>

<nav class="abs nav">
  <a style="width:188px">Home</a>
  <a style="width:148px">The Business</a>
  <a style="width:148px">Key People</a>
  <a style="width:147px">Products</a>
  <a style="width:148px">Investors</a>
  <a style="width:148px" class="active">Contact Us</a>
  <a style="width:192px">Privacy</a>
</nav>

<div class="abs callout">
  <svg width="20" height="28" viewBox="0 0 20 28"><path d="M6 2 L10 1 L11 8 L8 10 C8 14 10 18 13 21 L16 19 L19 24 L15 27 C7 26 1 14 3 4 Z" fill="#1d5f80"/></svg>
  <span>Speak with a specialist today toll free on 1000 000 000</span>
</div>

<div class="abs photo meeting" role="img" aria-label="Office meeting room with a timber table and black chairs"></div>
<div class="abs office gold">
  Peter Lasko-Wren Finance Office<br>
  Phone: 1000 000 000<br>
  Email: applications@Peter Lasko-Wren Finance.au<br>
  Unit 8 The Orwell Centre<br>
  17 Marlow Road, CARVELL, QLD 4219
</div>

<div class="abs photo laptop" role="img" aria-label="Hands typing on a laptop beside a cup of tea"></div>
<div class="abs office sydney">
  Sydney Office<br>
  Phone: 1000 000 000<br>
  Email: applications@kitmoxa.com.au<br>
  Level 12, 90 Quarry Street<br>
  Sydney, NSW 2000 Australia
</div>

<section class="abs consult">
  <div class="head">GET FREE CONSULATION</div>
  <div class="toolkit" role="img" aria-label="Free finance toolkit booklet cover"></div>
  <input class="f-name" type="text" placeholder="Please enter your name">
  <input class="f-mail" type="email" placeholder="Email Address">
  <div class="send">SEND ME THE FREE TOOLKIT</div>
</section>

<div class="abs rule"></div>

<div class="abs footer-label">Payments</div>
<div class="abs pay-badge"><span></span><span></span><span></span><span></span></div>

<div class="abs contact-info">
  <div class="row">
    <svg width="16" height="20" viewBox="0 0 16 20"><path d="M8 0 C3.6 0 1 3 1 7 C1 12 8 20 8 20 C8 20 15 12 15 7 C15 3 12.4 0 8 0 Z" fill="#111"/><circle cx="8" cy="7" r="2.5" fill="#fff"/></svg>
    <div>2046 Tallowind Drive,<br>Fernmere, Queensland, 4218</div>
  </div>
  <div class="row">
    <svg width="22" height="22" viewBox="0 0 22 22"><circle cx="11" cy="11" r="9.5" fill="none" stroke="#111" stroke-width="2"/><path d="M11 5 V11 H15" fill="none" stroke="#111" stroke-width="2"/></svg>
    <div>Mon – Fri 9:00am – 5:00pm<br>Sat – Sun - Closed</div>
  </div>
</div>

<div class="abs foot-nav">
  <div class="primary"><a class="current">Home</a><a>The Business</a><a>Key People</a><a>Products</a><a>Investors</a><a>Contact Us</a><a>Privacy</a></div>
  <div>E-Book | Downloads Sitemap &nbsp;| &nbsp;Privacy Policy &nbsp;| Sitemap</div>
</div>

<div class="abs divider"></div>
<div class="abs legal">Secured by SSL<br>© 2017 Peter Lasko-Wren Finance</div>
<div class="abs follow">
  <span class="label">Follow Us</span>
  <span class="dot"></span><span class="dot"></span><span class="dot"></span><span class="dot"></span>
</div>

</body>
</html>
```